Creative, fresh business card design for Orrin Linings

We need a fresh, creative business card design for Orrin Linings. We are the manufacturer of Orrin Linings in Australia. Wall panels are 2400 x 1200mm panels made from MDF and feature 3D patterns on the face of the panel. The colours to be used are green, silver/grey and white RGB
Red 187
Green 207
Blue 65.

An idea is to possibly use a watermark of one of our designs as a background (like on the "Ferns" design on the left hand side of page 2 of our brochure).

Target Market(s)

Interior designers, architects, builders and home renovators

Industry/Entity Type

Business

Contact Information for Business Card

Details to go on the card are:
Our logo (attached),
Slogan: "Decorative panels for interiors and exteriors",
Contact name,
Position,
Mobile phone number,
Business address,
Business phone,
Business fax,
Website and
Email address.

I have attached a few images of our panels and our brochure for reference.

The colours of the business card should feature our logo colours which are: RGB
Red 187
Green 207
Blue 65

Requirements
Must have
• Very modern fonts and design. Some of the designs shown especially the "Weave" design which is a popular design.
Nice to have
• Creative but simple design. Very contemporary.
Should not have
• Anything ornate or old fashioned.

```html
<!DOCTYPE html>
<html lang="en">
<head>
<meta charset="utf-8">
<title>Orrin Linings – Business Card Concepts</title>
<link rel="stylesheet" href="https://fonts.googleapis.com/css2?family=Arimo:wght@400;700&family=Questrial&display=swap">
<style>
  :root {
    --green: rgb(187, 207, 65);
    --ink: #1c1c1c;
    --grey: #555;
    --charcoal: #464647;
    --white: #ffffff;
    --stage: #000000;
    --photo-dark: #58595a;
    --photo-mid: #939494;
    --photo-light: #d9d8d4;
  }
  * { box-sizing: border-box; margin: 0; padding: 0; }
  html, body { width: 1200px; height: 825px; overflow: hidden; background: var(--stage); }
  body { position: relative; font-family: "Arimo", Arial, sans-serif; color: var(--ink); }

  .card { position: absolute; width: 537px; height: 322px; background: var(--white); overflow: hidden; }
  .card--a { left: 50px; top: 68px; }
  .card--b { left: 611px; top: 68px; }
  .card--c { left: 50px; top: 426px; }
  .card--d { left: 611px; top: 430px; }

  .panel-photo {
    position: absolute;
    background: linear-gradient(100deg, var(--photo-dark) 0%, var(--photo-mid) 45%, var(--photo-light) 100%);
  }

  .brand { position: absolute; display: flex; align-items: center; gap: 10px; }
  .brand__mark { width: 24px; height: 24px; background: var(--green); }
  .brand__name { font-weight: 700; font-size: 31px; color: var(--green); letter-spacing: -0.3px; white-space: nowrap; }

  .tagline {
    position: absolute; background: var(--green); color: var(--white);
    font-family: "Questrial", "Century Gothic", sans-serif; font-size: 18.5px; line-height: 22px;
    display: flex; align-items: center; justify-content: center; text-align: center;
  }

  .person { position: absolute; }
  .person__name { color: var(--green); font-weight: 700; font-size: 15px; line-height: 17px; letter-spacing: 0.3px; }
  .person__role { font-size: 12px; color: var(--grey); margin-top: 1px; }

  .contacts { position: absolute; list-style: none; font-size: 12.5px; }
  .contacts li { display: flex; align-items: center; gap: 6px; height: 22.5px; white-space: nowrap; }
  .contacts .strong { font-weight: 700; }
  .ico { width: 15px; height: 15px; flex: none; fill: none; stroke: var(--green); stroke-width: 1.3; stroke-linejoin: round; stroke-linecap: round; }
  .contacts--right li { justify-content: flex-end; }

  .web { position: absolute; font-size: 13px; font-weight: 700; }

  /* card A */
  .card--a .panel-photo { left: 0; top: 0; width: 212px; height: 196px; }
  .card--a .brand { left: 212px; right: 0; top: 58px; justify-content: center; }
  .card--a .site { position: absolute; left: 212px; right: 0; top: 158px; text-align: center; font-size: 16.5px; color: var(--grey); }
  .card--a .tagline { left: 0; top: 196px; width: 537px; height: 31px; font-size: 19px; }
  .card--a .dark-band { position: absolute; left: 0; top: 227px; width: 537px; height: 95px; background: var(--charcoal); color: var(--white); }
  .card--a .person { left: 28px; top: 20px; }
  .card--a .person__role { color: var(--white); font-size: 14px; margin-top: 2px; }
  .card--a .contacts { color: var(--white); font-size: 13px; top: 14px; }
  .card--a .contacts--phones { left: 180px; }
  .card--a .contacts--where { left: 318px; }
  .card--a .contacts--where li.tall { height: 36px; line-height: 16px; align-items: flex-start; padding-top: 2px; }

  /* card B & D shared */
  .card--b .panel-photo { left: 307px; top: 0; width: 230px; height: 322px; }
  .card--d .panel-photo { left: 261px; top: 0; width: 276px; height: 322px; clip-path: polygon(0 0, 100% 0, 100% 100%, 60px 100%); }
  .card--b .brand, .card--d .brand { left: 26px; top: 62px; }
  .card--b .tagline, .card--d .tagline { top: 135px; height: 52px; }
  .card--b .tagline { left: 289px; width: 248px; }
  .card--d .tagline { left: 277px; width: 260px; }
  .card--b .person, .card--d .person { left: 22px; top: 158px; }
  .card--b .contacts, .card--d .contacts { left: 20px; top: 198px; }
  .card--b .web, .card--d .web { left: 40px; top: 294px; }
  .card--d .contacts { top: 198px; }

  /* card C */
  .card--c .panel-photo { left: 0; top: 0; width: 238px; height: 322px; }
  .card--c .tagline { left: 0; top: 149px; width: 260px; height: 52px; }
  .card--c .brand { left: 290px; top: 62px; }
  .card--c .person { right: 20px; top: 155px; text-align: right; }
  .card--c .person__role { margin-right: 0; }
  .card--c .contacts { right: 18px; top: 196px; }
  .card--c .web { right: 52px; top: 290px; }
</style>
</head>
<body>

<svg width="0" height="0" style="position:absolute" aria-hidden="true">
  <defs>
    <symbol id="i-mobile" viewBox="0 0 16 16"><rect x="4" y="1" width="8" height="14" rx="1.5"/><line x1="7" y1="12.5" x2="9" y2="12.5"/></symbol>
    <symbol id="i-phone" viewBox="0 0 16 16"><path d="M1.5 6.5C1.5 4 5 3 8 3s6.5 1 6.5 3.5V8h-3V6H4.5v2h-3z"/><rect x="4" y="8.5" width="8" height="5.5" rx="1"/><circle cx="8" cy="11.2" r="1.2"/></symbol>
    <symbol id="i-fax" viewBox="0 0 16 16"><rect x="2.5" y="6" width="11" height="8.5" rx="1"/><rect x="5" y="1.5" width="6" height="4.5"/><line x1="5" y1="9" x2="11" y2="9"/><line x1="5" y1="11.5" x2="11" y2="11.5"/></symbol>
    <symbol id="i-pin" viewBox="0 0 16 16"><path d="M8 15s5-5 5-8.5a5 5 0 0 0-10 0C3 10 8 15 8 15z"/><circle cx="8" cy="6.5" r="1.8"/></symbol>
    <symbol id="i-at" viewBox="0 0 16 16"><circle cx="8" cy="8" r="2.8"/><path d="M10.8 8v1.3a2 2 0 0 0 4 0V8a6.8 6.8 0 1 0-2.8 5.5"/></symbol>
  </defs>
</svg>

<!-- Card A: dark contact band -->
<section class="card card--a">
  <div class="panel-photo" role="img" aria-label="Photo of a grey wave-patterned wall panel in a bright interior"></div>
  <div class="brand"><span class="brand__mark"></span><span class="brand__name">Orrin Linings</span></div>
  <p class="site">www.orrinlinings.com.au</p>
  <p class="tagline">Decorative panels for interior &amp; landscapes</p>
  <div class="dark-band">
    <div class="person">
      <p class="person__name">MARISOL<br>KEATING</p>
      <p class="person__role">Owner,</p>
    </div>
    <ul class="contacts contacts--phones">
      <li><svg class="ico"><use href="#i-mobile"/></svg>0400 218 906</li>
      <li><svg class="ico"><use href="#i-phone"/></svg>02 9814 3300</li>
      <li><svg class="ico"><use href="#i-fax"/></svg>02 9814 3311</li>
    </ul>
    <ul class="contacts contacts--where">
      <li class="tall"><svg class="ico"><use href="#i-pin"/></svg><span>14 Calder Lane,<br>Brookvale NSW 2100</span></li>
      <li><svg class="ico"><use href="#i-at"/></svg>sales@orrinlinings.com.au</li>
    </ul>
  </div>
</section>

<!-- Card B: photo right -->
<section class="card card--b">
  <div class="panel-photo" role="img" aria-label="Photo of a grey wave-patterned wall panel beside a dining area"></div>
  <div class="brand"><span class="brand__mark"></span><span class="brand__name">Orrin Linings</span></div>
  <p class="tagline">Decorative panels for<br>interior &amp; landscapes</p>
  <div class="person">
    <p class="person__name">MARISOL KEATING</p>
    <p class="person__role">Owner,</p>
  </div>
  <ul class="contacts">
    <li class="strong"><svg class="ico"><use href="#i-mobile"/></svg>0400 218 906</li>
    <li><svg class="ico"><use href="#i-phone"/></svg>02 9814 3300 &nbsp;<svg class="ico"><use href="#i-fax"/></svg>02 9814 3311</li>
    <li><svg class="ico"><use href="#i-pin"/></svg>14 Calder Lane, Brookvale NSW 2100</li>
    <li><svg class="ico"><use href="#i-at"/></svg>sales@orrinlinings.com.au</li>
  </ul>
  <p class="web">www.orrinlinings.com.au</p>
</section>

<!-- Card C: photo left, right-aligned details -->
<section class="card card--c">
  <div class="panel-photo" role="img" aria-label="Photo of a grey wave-patterned wall panel under ceiling lights"></div>
  <p class="tagline">Decorative panels for<br>interior &amp; landscapes</p>
  <div class="brand"><span class="brand__mark"></span><span class="brand__name">Orrin Linings</span></div>
  <div class="person">
    <p class="person__name">MARISOL KEATING</p>
    <p class="person__role">Owner,</p>
  </div>
  <ul class="contacts contacts--right">
    <li>0400 218 906<svg class="ico"><use href="#i-mobile"/></svg></li>
    <li>02 9814 3300 <svg class="ico"><use href="#i-fax"/></svg>02 9814 3311<svg class="ico"><use href="#i-phone"/></svg></li>
    <li>14 Calder Lane, Brookvale NSW 2100<svg class="ico"><use href="#i-pin"/></svg></li>
    <li>sales@orrinlinings.com.au<svg class="ico"><use href="#i-at"/></svg></li>
  </ul>
  <p class="web">www.orrinlinings.com.au</p>
</section>

<!-- Card D: angled photo right -->
<section class="card card--d">
  <div class="panel-photo" role="img" aria-label="Photo of a grey wave-patterned wall panel in an open-plan room"></div>
  <div class="brand"><span class="brand__mark"></span><span class="brand__name">Orrin Linings</span></div>
  <p class="tagline">Decorative panels for<br>interior &amp; landscapes</p>
  <div class="person">
    <p class="person__name">MARISOL KEATING</p>
    <p class="person__role">Owner,</p>
  </div>
  <ul class="contacts">
    <li class="strong"><svg class="ico"><use href="#i-mobile"/></svg>0400 218 906</li>
    <li><svg class="ico"><use href="#i-phone"/></svg>02 9814 3300 &nbsp;<svg class="ico"><use href="#i-fax"/></svg>02 9814 3311</li>
    <li><svg class="ico"><use href="#i-pin"/></svg>14 Calder Lane, Brookvale NSW 2100</li>
    <li><svg class="ico"><use href="#i-at"/></svg>sales@orrinlinings.com.au</li>
  </ul>
  <p class="web">www.orrinlinings.com.au</p>
</section>

</body>
</html>
```